Business Card Upgrade

I have designed our business card using our new logo. I think it needs imporovements. We used to have two cards for our business. One card was for our software business, and the other was for our consulting business. We are now in the process of combining our websites, marketing, name, and a new logo.

Our goal is to have a really sharp professional logo. One reason I designed the card the way I did was that our Titles are sometimes long, and by separating the person's name and title, it shows up very well and the title can be adjusted no matter how long it is. Sometimes the title can be 4 or 5 words or more.

We really like our logo on black as it shows up very nice. Our PMS colors are as follows: 368C and 459C.

The Designer that will be working with us will need to deliver the following:

The front and back of the Business Card Design will need to be delivered in a high quality JPEG, and
The front and back of the Business Card Design in Illustrator Format .ai
Any fonts will need to be sent to us if they are not standard and are required to open the Illustrator file correctly.

To help us get a good idea of the card with a title, please use the title: " Director of Software Development "

NOTE: The chosen designer will be selected to design our new letterhead within 2 weeks from the closing of this contest.

To help us make sure the card design works with longer titles, please use the followign job title on the card:  

"Director of Software and Product Development"

 

ALL DESIGNERS:

1. I appreciate the different angles you are showing the cards, but please be sure and always show the direct view, so I can see the layout and what the person I hand the card will see.

2. Please do not use white.  Please use off white as I don't care for white cards and they get dirty easy and do not represent the designs well.

Dear Designers,

Please provide samples straight one as a viewer of the card will see.  Some of the angles that are presented make it impossible to tell how everything fits, and sometimes even makes areas look skewed. So, please provide a straight sample view.

Pinnacle 400 company executives such as Vice Presidents, and Directors

Software

• Professional looking Card.

Our customers are Directors, Vice Presidents, and Presidents of companies as large as Pinnacle 400 companies. The card needs to get attention wile still looking professional.

Delivery of the finished product in Illustrator Format with any fonts needed to edit the text or open the file.

The card will be a heavy stock with a soft touch coating for that silk feel.

```html
<!DOCTYPE html>
<html lang="en">
<head>
<meta charset="utf-8">
<title>Kestrel Trade – Business Card</title>
<link href="https://fonts.googleapis.com/css2?family=Open+Sans:wght@400;600;700&display=swap" rel="stylesheet">
<style>
  :root {
    --stage: #e9e5de;
    --card: #060606;
    --green: #5db446;
    --gold: #dccb86;
    --ink: #f4f1ea;
    --shadow: rgba(0, 0, 0, 0.45);
  }
  * { box-sizing: border-box; margin: 0; padding: 0; }
  html, body {
    width: 1200px;
    height: 900px;
    overflow: hidden;
    background: var(--stage);
    font-family: "Open Sans", Arial, sans-serif;
  }
  .stage { position: relative; width: 1200px; height: 900px; }
  .card {
    position: absolute;
    width: 585px;
    height: 333px;
    background: var(--card);
    box-shadow: -4px 6px 10px var(--shadow);
    overflow: hidden;
  }
  .card-front { left: 93px; top: 107px; }
  .card-back { left: 535px; top: 497px; }

  .wordmark {
    position: absolute;
    left: 0;
    right: 0;
    text-align: center;
    color: var(--green);
    font-weight: 700;
    letter-spacing: 3px;
    line-height: 1;
  }
  .card-front .wordmark { top: 176px; font-size: 34px; top: 70px; }
  .card-back .wordmark { top: 155px; font-size: 40px; }

  .person { position: absolute; left: 37px; top: 177px; }
  .person-name {
    color: var(--green);
    font-size: 22px;
    font-weight: 600;
    line-height: 1;
  }
  .person-title {
    color: var(--gold);
    font-size: 12px;
    margin-top: 5px;
  }
  .contact-list {
    position: absolute;
    left: 37px;
    top: 232px;
    list-style: none;
    color: var(--ink);
    font-size: 12.5px;
    line-height: 14.5px;
  }
  .contact-list li { display: flex; align-items: center; }
  .contact-list svg { width: 11px; height: 11px; margin-right: 16px; fill: var(--green); }
  .office {
    position: absolute;
    right: 31px;
    top: 226px;
    text-align: right;
    color: var(--ink);
    font-size: 12.5px;
    line-height: 16.5px;
  }
  .office .site { margin-top: 3px; }

  .dot-field {
    position: absolute;
    inset: 0;
    background:
      linear-gradient(150deg, transparent 30%, rgba(120,120,120,0.35) 42%, rgba(60,60,60,0.15) 52%, transparent 62%),
      linear-gradient(330deg, rgba(90,90,90,0.3) 0%, rgba(70,70,70,0.15) 18%, transparent 32%),
      linear-gradient(150deg, rgba(70,70,70,0.3) 0%, transparent 22%);
  }
  .back-site {
    position: absolute;
    left: 0;
    right: 0;
    top: 296px;
    text-align: center;
    color: var(--ink);
    font-size: 14px;
  }
  .back-site .accent { color: var(--green); }
</style>
</head>
<body>
<main class="stage">
  <section class="card card-front" aria-label="Card front">
    <div class="wordmark">KESTREL TRADE</div>
    <div class="person">
      <h1 class="person-name">DANIEL HART</h1>
      <p class="person-title">Director of Software and Product Development</p>
    </div>
    <ul class="contact-list">
      <li><svg viewBox="0 0 12 12"><path d="M2.5 0.5l2 2.5-1 1.3c.7 1.6 2 2.9 3.6 3.6l1.3-1 2.5 2-1.2 2.3C5 11 1 7 0.3 1.7z"/></svg>000 0 0000000</li>
      <li><svg viewBox="0 0 12 12"><path d="M3 0h6v12H3zM4 1.5v8h4v-8z"/></svg>000 0 0000000</li>
      <li><svg viewBox="0 0 12 12"><path d="M0 2h12v1.2L6 7 0 3.2zM0 4.6l6 3.8 6-3.8V10H0z"/></svg>name@domainname.com</li>
    </ul>
    <address class="office" style="font-style:normal">
      <p>Your Office Address Goes Here,</p>
      <p>City, Zip Code, Country Name</p>
      <p class="site">www.websitename.com</p>
    </address>
  </section>

  <section class="card card-back" aria-label="Card back">
    <div class="dot-field" role="img" aria-label="Diagonal grey halftone dot pattern fading across the card"></div>
    <div class="wordmark">KESTREL TRADE</div>
    <p class="back-site">www.<span class="accent">websitename</span>.com</p>
  </section>
</main>
</body>
</html>
```